Business Card - Rebranding for Consulting Firm

We are renaming and rebranding our consulting firm and need to raise the level of quality of our cards as part of that effort. We consult to leading high tech, life science and other innovation sector companies.

Need a two-sided business card design.

Side 1: (a) Company logo (b) tag line: Optimize Your Investment in Talent (c) Name (d) Title (e) Phone 1: Office (f) Phone 2: Mobile (g) email: person@HollowmereAdvisory.com

Side 2: Two lines of text: (a) Growth is Imperative. Change is Constant. Talent Executes Strategy. (b) We help you excel at all three.

Target Market(s)

Business and human resources executives and senior managers

Industry/Entity Type

Management Consulting

Contact Information for Business Card

Font styles to use
Sans Serif

Requirements
Must have
• clean, not too busy, but with a bit of creativity. Stick to the colors used in the attached logo
• appeal to high tech, life science companies
Nice to have
• prefer white background

```html
<!DOCTYPE html>
<html lang="en">
<head>
<meta charset="utf-8">
<title>Hollowmere Advisory – Business Card</title>
<link rel="stylesheet" href="https://fonts.googleapis.com/css2?family=Bebas+Neue&family=Lato:wght@400;700&display=swap">
<style>
  :root {
    --blue: #0a68a8;
    --blue-light: #1aa3dd;
    --grey-band: #6f6f6f;
    --text-dark: #3c3c3c;
    --text-mid: #555555;
    --page: #ececec;
    --card: #fbfbfb;
    --divider: #c4c4c4;
  }
  * { margin: 0; padding: 0; box-sizing: border-box; }
  html, body { width: 1200px; height: 586px; overflow: hidden; }
  body { background: var(--page); position: relative; font-family: "Lato", sans-serif; }

  .card {
    position: absolute; top: 129px; width: 502px; height: 301px;
    background: var(--card); overflow: hidden;
    box-shadow: 0 2px 6px rgba(0,0,0,0.12);
  }
  .card--back { left: 65px; }
  .card--front { left: 608px; }

  .card__band { position: absolute; left: 0; bottom: 0; width: 502px; height: 18px; display: block; }

  /* Back side */
  .manifesto {
    position: absolute; left: 0; right: 0; top: 44px;
    font-family: "Bebas Neue", sans-serif; color: var(--blue);
    font-size: 44px; line-height: 52px; text-align: center; letter-spacing: 0.2px;
  }
  .promise {
    position: absolute; left: 106px; width: 290px; top: 233px; height: 25px;
    border-top: 1.5px solid var(--blue); border-bottom: 1.5px solid var(--blue);
    color: var(--blue); font-weight: 700; font-size: 12.5px;
    display: flex; align-items: center; justify-content: center;
  }

  /* Front side */
  .brand {
    position: absolute; left: 0; right: 0; top: 52px;
    display: flex; align-items: center; justify-content: center; gap: 12px;
  }
  .brand__mark { width: 26px; height: 26px; background: var(--blue); }
  .brand__name { font-size: 38px; font-weight: 400; color: var(--blue); letter-spacing: -0.5px; }

  .tagline {
    position: absolute; left: 0; right: 0; top: 119px;
    display: flex; align-items: center; justify-content: center; gap: 6px;
    color: var(--blue); font-weight: 700; font-size: 12px;
  }
  .tagline__rule { width: 53px; height: 2px; background: var(--blue); }

  .person { position: absolute; right: 312px; top: 209px; text-align: right; white-space: nowrap; }
  .person__name { color: var(--blue); font-weight: 700; font-size: 16px; }
  .person__title { color: var(--text-mid); font-size: 12.5px; margin-top: 3px; }

  .divider {
    position: absolute; left: 213px; top: 175px; width: 2px; height: 88px;
    background: linear-gradient(to bottom, transparent, var(--divider) 25%, var(--divider) 75%, transparent);
  }

  .contacts { position: absolute; left: 234px; top: 191px; list-style: none; }
  .contacts li {
    display: flex; align-items: center; gap: 8px; height: 24.5px;
    font-weight: 700; font-size: 12px; color: var(--text-dark);
  }
  .contacts svg { width: 13px; height: 12px; fill: var(--blue); flex: none; }
</style>
</head>
<body>

  <section class="card card--back" aria-label="Business card, back">
    <h1 class="manifesto">Growth is imperative.<br>Change is constant.<br>Talent executes strategy.</h1>
    <p class="promise">WE HELP YOU EXCEL AT ALL THREE.</p>
    <svg class="card__band" viewBox="0 0 502 18" aria-hidden="true">
      <rect x="0" y="6" width="502" height="12" fill="var(--grey-band)"/>
      <path d="M292 18 Q300 0 326 0 H502 V18 Z" fill="#ffffff"/>
      <path d="M298 18 Q306 3 330 3 H502 V18 Z" fill="var(--blue)"/>
    </svg>
  </section>

  <section class="card card--front" aria-label="Business card, front">
    <div class="brand">
      <span class="brand__mark"></span>
      <span class="brand__name">Hollowmere Advisory</span>
    </div>
    <p class="tagline"><span class="tagline__rule"></span>Optimize Your Investment in Talent<span class="tagline__rule"></span></p>

    <div class="person">
      <p class="person__name">Dana Whitcombe</p>
      <p class="person__title">Founder / Director</p>
    </div>
    <div class="divider"></div>

    <ul class="contacts">
      <li>
        <svg viewBox="0 0 13 12" aria-label="Office"><path d="M1 4 Q6.5 0 12 4 L11 5.5 9 5 8.5 3.5 Q6.5 3 4.5 3.5 L4 5 2 5.5Z M3 6 H10 L11 11 H2Z"/></svg>
        (555) 214-0187
      </li>
      <li>
        <svg viewBox="0 0 13 12" aria-label="Mobile"><path d="M3 1 H10 V4 H3Z M1 4.5 H12 V9 H10 V7 H3 V9 H1Z M3.5 7.5 H9.5 V11 H3.5Z"/></svg>
        (555) 309-4462
      </li>
      <li>
        <svg viewBox="0 0 13 12" aria-label="Email"><path d="M0.5 2 H12.5 V10.5 H0.5Z" /><path d="M0.5 2 L6.5 7 L12.5 2 M0.5 10.5 L5 6 M12.5 10.5 L8 6" stroke="#fbfbfb" stroke-width="1" fill="none"/></svg>
        person@HollowmereAdvisory.com
      </li>
    </ul>

    <svg class="card__band" viewBox="0 0 502 18" aria-hidden="true">
      <rect x="0" y="6" width="502" height="12" fill="var(--grey-band)"/>
      <path d="M292 18 Q300 0 326 0 H502 V18 Z" fill="#ffffff"/>
      <path d="M298 18 Q306 3 330 3 H502 V18 Z" fill="var(--blue)"/>
    </svg>
  </section>

</body>
</html>
```